Cover für Gedichtbuch
Zielgruppe
Das Buch soll jungen und alten Menschen gefallen. Zielgruppe sind aber vor allem junge Leser zwischen 18 und Mitte 20.
Aufgabenstellung
Für das Erstlingswerk von zwei Nachwuchsautoren wird ein Wendecover gesucht. Sprich: Auf der einen Seite stehen Gedichte mit hellen Gedichten (Liebe, Freude, Glück) - die andere Hälfte besteht aus dunklen Gedichten (Tod, Depression). Das Buch soll gedreht werden. Daher sollen die beiden Coverseiten einen Kontrast darstellen.

```html
<!DOCTYPE html>
<html lang="de">
<head>
<meta charset="utf-8">
<title>Helle Gedichte – Buchcover</title>
<link rel="stylesheet" href="https://fonts.googleapis.com/css2?family=Damion&family=Raleway:wght@300&display=swap">
<style>
  :root {
    --leaf-green: #9cc41c;
    --circle-green: #a9cd2c;
    --white: #ffffff;
    --author: #eef5d2;
    --band-teal: #86cbbe;
    --band-blue: #a4d4ca;
    --band-pale: #cfe08c;
    --band-sand: #e8d97c;
    --band-gold: #f1c466;
    --band-orange: #f4ac4e;
  }
  html, body {
    margin: 0;
    padding: 0;
    width: 844px;
    height: 1200px;
    overflow: hidden;
    background: var(--leaf-green);
  }
  .cover {
    position: relative;
    width: 844px;
    height: 1200px;
    overflow: hidden;
  }
  .cover__pattern {
    position: absolute;
    inset: 0;
    background: var(--leaf-green);
  }
  .cover__waves {
    position: absolute;
    inset: 0;
  }
  .title-disc {
    position: absolute;
    left: 200px;
    top: 180px;
    width: 410px;
    height: 410px;
    border-radius: 50%;
    background: var(--circle-green);
  }
  .title-disc__title {
    position: absolute;
    left: 290px;
    top: 290px;
    margin: 0;
    font-family: "Damion", cursive;
    font-weight: 400;
    font-size: 64px;
    line-height: 62px;
    color: var(--white);
    transform: rotate(-4deg);
    transform-origin: left top;
  }
  .title-disc__rule {
    position: absolute;
    left: 290px;
    top: 455px;
    width: 252px;
    height: 2px;
    background: var(--white);
  }
  .title-disc__author {
    position: absolute;
    left: 290px;
    top: 496px;
    width: 252px;
    margin: 0;
    text-align: center;
    font-family: "Raleway", sans-serif;
    font-weight: 300;
    font-size: 22px;
    color: var(--author);
  }
</style>
</head>
<body>
<main class="cover">
  <div class="cover__pattern" role="img" aria-label="Grünes Streumuster aus kleinen dunkelgrünen Blütenornamenten"></div>

  <svg class="cover__waves" width="844" height="1200" viewBox="0 0 844 1200" aria-hidden="true">
    <path fill="var(--band-teal)"   d="M0,930 C260,900 560,760 844,590 L844,1200 L0,1200 Z"/>
    <path fill="var(--band-blue)"   d="M0,990 C270,960 560,850 844,700 L844,1200 L0,1200 Z"/>
    <path fill="var(--band-pale)"   d="M0,1040 C280,1010 570,930 844,800 L844,1200 L0,1200 Z"/>
    <path fill="var(--band-sand)"   d="M0,1090 C290,1065 580,1000 844,900 L844,1200 L0,1200 Z"/>
    <path fill="var(--band-gold)"   d="M0,1135 C300,1115 590,1070 844,990 L844,1200 L0,1200 Z"/>
    <path fill="var(--band-orange)" d="M0,1175 C310,1160 600,1140 844,1080 L844,1200 L0,1200 Z"/>
  </svg>

  <div class="title-disc"></div>
  <h1 class="title-disc__title">Helle<br>Gedichte</h1>
  <div class="title-disc__rule"></div>
  <p class="title-disc__author">Bernhard Wulf</p>
</main>
</body>
</html>
```